依頼詳細
◆デザインのイメージ
・『営業』『広告』の雰囲気ではなく、一見『ご家庭用の年賀状』の雰囲気
・とにかく可愛い、柔らかくほのぼのとした感じ、愛らしい感じ
『仲の良い友達からの可愛い年賀状』のイメージ
・干支もさりげなく登場していると嬉しいです
・一言コメントを書けるスペースが少しあると助かります
・「天地左右5mmの余白」が必要
印刷可能範囲は「90mm×138mm」となります。

ご不明な点がございましたらお気軽にご連絡ください。

よろしくお願いします。

記載項目
◆文字原稿を添付いたします
◆印刷はソラノ刷版に依頼致します
◆納品はPDFまたはJPGでお願いします
◆店舗名は無くても大丈夫です(宛先面に差出人印刷をします)

希望イメージ
シンプル 複雑
単色 カラフル
暗い 明るい
日常 高級
遊び心 厳粛
未来的 伝統的
女性的 男性的
補足説明
サロンHP
https://mafuwa.info
■ 選んだ理由

今回は当サロンスタッフの投票で当選作品を決定させていただきました。

■ 提案者全員のお礼・コメント

ご提案頂きました皆様、この度は誠に有難うございます。
素敵な作品ばかりで毎回当選作品を1つに絞るのが心苦しいです。
また機会がございましたらどうぞよろしくお願いします。

```html
<!DOCTYPE html>
<html lang="ja">
<head>
<meta charset="utf-8">
<title>2022 年賀状</title>
<link rel="stylesheet" href="https://fonts.googleapis.com/css2?family=Kosugi+Maru&family=M+PLUS+Rounded+1c:wght@500;800&family=Fredoka:wght@600;700&display=swap">
<style>
  :root{
    --paper:#ffffff;
    --border-gold:#f6d27a;
    --border-light:#fcecc0;
    --orange:#f29a1f;
    --orange-deep:#ee8a0c;
    --green:#8cc43f;
    --ink:#333333;
    --muted:#555555;
    --art-warm:#f7c873;
    --art-red:#e8614b;
  }
  *{margin:0;padding:0;box-sizing:border-box}
  html,body{width:809px;height:1200px;overflow:hidden;background:var(--paper)}
  body{font-family:"M PLUS Rounded 1c","Kosugi Maru",sans-serif;color:var(--ink)}
  .card{position:relative;width:809px;height:1200px;background:var(--paper)}
  .side-pattern{position:absolute;top:0;width:64px;height:1200px;
    background:linear-gradient(180deg,var(--border-gold),var(--border-light),var(--border-gold))}
  .side-pattern.left{left:0}
  .side-pattern.right{right:0}
  .greeting-arc{position:absolute;left:60px;top:0;width:690px;height:230px}
  .greeting-arc text{font-family:"Fredoka",sans-serif;font-weight:600;font-size:50px;fill:var(--green);letter-spacing:4px}
  .zodiac-art{position:absolute;left:250px;top:100px;width:310px;height:420px;border-radius:48% 48% 46% 46%;
    background:radial-gradient(circle at 50% 28%,var(--art-red) 0 18%,var(--art-warm) 42%,#fbe6b5 72%,transparent 73%)}
  .year{position:absolute;left:0;width:809px;top:505px;text-align:center;font-family:"Fredoka",sans-serif;
    font-weight:700;font-size:60px;color:#111;letter-spacing:2px}
  .message{position:absolute;left:0;width:809px;top:598px;text-align:center;font-size:25px;line-height:38px;font-weight:500}
  .message .opening{color:var(--orange-deep)}
  .message .dated{font-size:16px;color:var(--muted);margin-left:8px}
  .voucher{position:absolute;left:112px;top:705px;width:596px;height:110px;border:3px solid var(--orange);
    border-radius:10px;display:flex;background:#fff}
  .voucher-tab{width:140px;background:var(--orange);color:#fff;font-size:15px;line-height:22px;
    display:flex;align-items:center;justify-content:center;text-align:center;border-radius:5px 0 0 5px}
  .voucher-body{flex:1;text-align:center;color:var(--orange-deep);padding-top:8px}
  .voucher-amount{font-size:50px;font-weight:800;line-height:58px}
  .voucher-amount small{font-size:30px}
  .voucher-term{font-size:20px;font-weight:500}
  .conditions{position:absolute;left:112px;top:868px;width:600px;font-size:25px;line-height:38px;font-weight:500}
  .notes{position:absolute;left:112px;top:955px;font-size:15px;line-height:22px;color:var(--muted)}
  .chat-box{position:absolute;left:112px;top:1040px;width:596px;height:92px;border:3px solid var(--orange);
    border-radius:10px;display:flex;overflow:hidden}
  .chat-tab{width:150px;background:var(--orange);color:#fff;text-align:center;display:flex;flex-direction:column;
    justify-content:center;font-weight:800}
  .chat-tab .name{font-size:22px}
  .chat-tab .sub{font-size:15px;font-weight:500}
  .chat-body{flex:1;display:flex;align-items:center;justify-content:center;text-align:center;font-size:21px;line-height:32px;font-weight:500}
</style>
</head>
<body>
<main class="card">
  <div class="side-pattern left" role="img" aria-label="黄色の市松模様の縁取り"></div>
  <div class="side-pattern right" role="img" aria-label="黄色の市松模様の縁取り"></div>

  <svg class="greeting-arc" viewBox="0 0 690 230" aria-label="A HAPPY NEW YEAR!">
    <defs><path id="arc" d="M10 215 Q345 -75 680 215"/></defs>
    <text><textPath href="#arc" startOffset="50%" text-anchor="middle">A HAPPY NEW YEAR !</textPath></text>
  </svg>

  <div class="zodiac-art" role="img" aria-label="しめ縄飾りと扇、招福の札を持つ寅のイラスト"></div>
  <div class="year">2022</div>

  <p class="message">
    今年もスタッフ一同技術向上に励んで参ります<br>
    <span class="opening">年始は8日(土)より営業いたします</span><span class="dated">2022年元旦</span>
  </p>

  <section class="voucher">
    <div class="voucher-tab">この年賀状を<br>ご持参ください</div>
    <div class="voucher-body">
      <div class="voucher-amount">金券2,000<small>円</small></div>
      <div class="voucher-term">有効期限令和4年2月末日</div>
    </div>
  </section>

  <p class="conditions">90分以上のコースでお会計より2000円<br>お値引きいたします! A・B・Cコースも可!</p>
  <p class="notes">※期間中1回ご利用頂けます　※オプション無料券と併用できます<br>※その他の割引との併用はできません</p>

  <section class="chat-box">
    <div class="chat-tab"><span class="name">トモチャット</span><span class="sub">お友達登録で</span></div>
    <div class="chat-body">WEB予約やマフワ花見台への<br>個別連絡にもご利用いただけます</div>
  </section>
</main>
</body>
</html>
```